Zielgruppe
Wir sind ein kleiner familiengeführter Weinbaubetrieb am Wagram und suchen einen modernen und naturnahen Namen und ein Etikett mit Blickfang für unseren Wermut, aus handgepflückten regionalen Wildkräutern mit Rosewein vom Zweigelt. Charakeristik des Getränks: Aperitif, Zitrusnote, leichte Bitternote, mit Tonic water als Cocktail.
Unsere Zielgruppe: kaufkräftige Genussmenschen im mittleren Alter
Aufgabenstellung
Etikett für 0,5l Flasche, Flasche noch nicht festgelegt, Etikettenhöhe: 65mm
Was soll draufstehen: Name, Vermouth, local botanicals, handcrafted, small batch

```html
<!DOCTYPE html>
<html lang="de">
<head>
<meta charset="utf-8">
<title>Lumea Wermuth – Etiketten</title>
<link href="https://fonts.googleapis.com/css2?family=Arimo:wght@300;400;700&display=swap" rel="stylesheet">
<style>
  :root {
    --page-bg: #ffffff;
    --ink: #2a1414;
    --ink-soft: #5a4a4a;
    --oval: #fdfdf8;
    --sun-orange: #f4a24a;
    --sun-yellow: #f7e27a;
    --mint: #a9d5c2;
    --sky: #7fb3dc;
    --lilac: #c78ad6;
    --mauve: #e2c6df;
    --sand: #ddd6c4;
    --sage: #8dbb80;
    --wing-light: #dfe4f7;
    --wing-dark: #6a58b8;
  }
  * { box-sizing: border-box; margin: 0; padding: 0; }
  html, body {
    width: 1200px; height: 1164px; overflow: hidden;
    background: var(--page-bg);
    font-family: "Arimo", Arial, sans-serif;
  }
  .label-sheet {
    position: relative; width: 1200px; height: 1164px;
    display: flex; justify-content: center; align-items: center; gap: 80px;
  }
  .label {
    position: relative; width: 480px; height: 728px; overflow: hidden;
    color: var(--ink);
  }
  .label--citrus {
    background:
      radial-gradient(ellipse at 100% 0%, var(--sun-orange) 0%, transparent 45%),
      linear-gradient(180deg, var(--sun-orange) 0%, var(--sun-yellow) 24%, #f3ecae 40%, var(--mint) 62%, var(--sky) 82%, #8cbde0 100%);
  }
  .label--herb {
    background:
      linear-gradient(180deg, var(--lilac) 0%, var(--mauve) 30%, #e6dcd8 48%, var(--sand) 60%, #b7cfa4 76%, var(--sage) 100%);
  }
  .name-oval {
    position: absolute; left: 101px; top: 26px; width: 304px; height: 172px;
    border-radius: 50%; background: var(--oval);
    text-align: center;
  }
  .name-oval__name {
    display: block; margin-top: 36px;
    font-size: 60px; font-weight: 400; line-height: 1; letter-spacing: 1px;
  }
  .name-oval__year {
    display: block; margin-top: 10px;
    font-size: 26px; font-weight: 700; line-height: 1;
  }
  .butterfly {
    position: absolute; left: 141px; top: 186px; width: 221px; height: 164px;
  }
  .product-title {
    position: absolute; left: 0; width: 480px; top: 380px;
    text-align: center; padding-right: 26px;
    font-size: 48px; font-weight: 700; letter-spacing: 0.5px; line-height: 1.1;
  }
  .product-desc {
    position: absolute; left: 0; width: 480px; top: 444px;
    text-align: center; padding-right: 26px;
    font-size: 17px; font-weight: 700; line-height: 1.4;
  }
  .product-claims {
    position: absolute; left: 0; width: 480px; top: 562px;
    text-align: center; padding-right: 26px;
    font-size: 16px; font-weight: 400; line-height: 1.45; letter-spacing: 0.5px;
  }
  .volume, .abv {
    position: absolute; top: 656px;
    font-size: 29px; font-weight: 300; color: var(--ink-soft); line-height: 1;
  }
  .volume { left: 64px; }
  .abv { right: 44px; }
</style>
</head>
<body>
<main class="label-sheet">

  <article class="label label--citrus">
    <div class="name-oval">
      <span class="name-oval__name">Lumea</span>
      <span class="name-oval__year">2021</span>
    </div>
    <svg class="butterfly" viewBox="0 0 221 164" role="img" aria-label="Aquarell-Illustration eines blau-violetten Schmetterlings">
      <defs>
        <radialGradient id="wing-citrus" cx="45%" cy="45%" r="60%">
          <stop offset="0%" stop-color="var(--wing-light)"/>
          <stop offset="100%" stop-color="var(--wing-dark)"/>
        </radialGradient>
      </defs>
      <ellipse cx="110" cy="82" rx="108" ry="80" fill="url(#wing-citrus)" opacity="0.85"/>
    </svg>
    <h1 class="product-title">WERMUTH</h1>
    <p class="product-desc">Aus handgepflückten<br>regionalen Wildkräutern<br>mit Rosewein vom Zwei-<br>gelt</p>
    <p class="product-claims">Vermouth · local botanicals<br>handcrafted · small batch</p>
    <span class="volume">0,5 l</span>
    <span class="abv">17 % vol</span>
  </article>

  <article class="label label--herb">
    <div class="name-oval">
      <span class="name-oval__name">Lumea</span>
      <span class="name-oval__year">2021</span>
    </div>
    <svg class="butterfly" viewBox="0 0 221 164" role="img" aria-label="Aquarell-Illustration eines blau-violetten Schmetterlings">
      <defs>
        <radialGradient id="wing-herb" cx="45%" cy="45%" r="60%">
          <stop offset="0%" stop-color="var(--wing-light)"/>
          <stop offset="100%" stop-color="var(--wing-dark)"/>
        </radialGradient>
      </defs>
      <ellipse cx="110" cy="82" rx="108" ry="80" fill="url(#wing-herb)" opacity="0.85"/>
    </svg>
    <h1 class="product-title">WERMUTH</h1>
    <p class="product-desc">Aus handgepflückten<br>regionalen Wildkräutern<br>mit Rosewein vom Zwei-<br>gelt</p>
    <p class="product-claims">Vermouth · local botanicals<br>handcrafted · small batch</p>
    <span class="volume">0,5 l</span>
    <span class="abv">17 % vol</span>
  </article>

</main>
</body>
</html>
```